Brightwave Business Card

Professional Business Card Design required using the attached contact information.

Contact information can be rearranged as required.

The company is a new start up venture developing solar systems, the branding should be in keeping with that of one of the investors whose website is as follows https://www.quorvex.com/

```html
<!DOCTYPE html>
<html lang="en">
<head>
<meta charset="UTF-8">
<title>Brightwave Renewables – Business Card</title>
<link href="https://fonts.googleapis.com/css2?family=Montserrat:wght@500;600;700&family=Arimo:wght@400&display=swap" rel="stylesheet">
<style>
  :root {
    --page-bg: #e6e8ea;
    --card-white: #ffffff;
    --ink: #111418;
    --brand-green: #2f7d5a;
    --back-green-light: #2f7a5c;
    --back-green-dark: #1f5a42;
    --navy-band: #2b313d;
    --teal-band: #3f97b4;
    --body-text: #2a2a2a;
  }
  * { box-sizing: border-box; margin: 0; padding: 0; }
  html, body { width: 1200px; height: 900px; overflow: hidden; }
  body {
    background: var(--page-bg);
    font-family: "Arimo", Arial, sans-serif;
    display: flex;
    flex-direction: column;
    align-items: center;
    justify-content: center;
    gap: 56px;
  }
  .card {
    position: relative;
    width: 600px;
    height: 343px;
    border-radius: 4px;
    overflow: hidden;
    box-shadow: 0 6px 18px rgba(0,0,0,0.18);
  }
  .card-front { background: var(--card-white); }
  .front-bands { position: absolute; inset: 0; width: 100%; height: 100%; }
  .brand-name {
    position: absolute;
    top: 30px; left: 34px; right: 34px;
    font-family: "Montserrat", sans-serif;
    font-weight: 700;
    font-size: 29px;
    letter-spacing: 1.5px;
    line-height: 1;
    color: var(--ink);
    text-transform: uppercase;
    white-space: nowrap;
    display: flex; align-items: center; gap: 12px;
  }
  .brand-dot {
    flex: none;
    width: 11px; height: 11px; border-radius: 50%;
    background: var(--brand-green);
  }
  .person-name {
    position: absolute;
    top: 88px; left: 34px;
    font-family: "Montserrat", sans-serif;
    font-weight: 600;
    font-size: 19px;
    font-variant: small-caps;
    letter-spacing: 1px;
    color: var(--brand-green);
  }
  .name-rule {
    position: absolute;
    top: 120px; left: 34px;
    width: 70px; height: 4px;
    background: var(--brand-green);
  }
  .contact-icons {
    position: absolute;
    top: 132px; left: 34px;
    display: flex; gap: 12px;
  }
  .contact-icons svg { width: 13px; height: 13px; }
  .contact-list {
    position: absolute;
    top: 158px; left: 34px;
    list-style: none;
    font-size: 12.5px;
    line-height: 19px;
    color: var(--body-text);
  }
  .company-legal {
    position: absolute;
    right: 30px; bottom: 26px;
    font-family: "Montserrat", sans-serif;
    font-weight: 500;
    font-size: 17px;
    letter-spacing: 5px;
    color: #ffffff;
    text-transform: uppercase;
    white-space: nowrap;
  }
  .card-back {
    background: linear-gradient(160deg, var(--back-green-light), var(--back-green-dark));
  }
</style>
</head>
<body>
  <section class="card card-front">
    <svg class="front-bands" viewBox="0 0 600 343" preserveAspectRatio="none" aria-hidden="true">
      <polygon points="0,262 205,262 190,343 0,343" fill="var(--teal-band)"/>
      <polygon points="205,262 600,262 600,343 175,343 190,290" fill="var(--navy-band)"/>
      <polygon points="170,262 215,262 205,278" fill="var(--card-white)"/>
    </svg>
    <div class="brand-name">Brightwave <span class="brand-dot"></span> Renewables</div>
    <div class="person-name">Daniel Merrow</div>
    <div class="name-rule"></div>
    <div class="contact-icons">
      <svg viewBox="0 0 16 16" aria-label="phone"><path d="M4 1.5l2.2 3-1.3 1.6c.8 1.8 2.2 3.2 4 4l1.6-1.3 3 2.2-1.2 2.6C7 13.5 2.5 9 1.4 2.7z" fill="var(--brand-green)"/></svg>
      <svg viewBox="0 0 16 16" aria-label="email"><rect x="1.5" y="3.5" width="13" height="9" fill="none" stroke="var(--brand-green)" stroke-width="1.5"/><path d="M1.5 3.5l6.5 5 6.5-5" fill="none" stroke="var(--brand-green)" stroke-width="1.5"/></svg>
      <svg viewBox="0 0 16 16" aria-label="address"><circle cx="8" cy="5" r="3" fill="none" stroke="var(--brand-green)" stroke-width="1.5"/><path d="M2.5 15c0-3.5 2.5-5 5.5-5s5.5 1.5 5.5 5z" fill="none" stroke="var(--brand-green)" stroke-width="1.5"/></svg>
    </div>
    <ul class="contact-list">
      <li>+1 (555) 014-2276</li>
      <li>daniel.merrow@brightwave-renewables.com</li>
      <li>418 Meridian Avenue, Boston, MA 02118</li>
    </ul>
    <div class="company-legal">Brightwave Renewables LLC</div>
  </section>

  <section class="card card-back" role="img" aria-label="Repeating diagonal pattern of the Brightwave Renewables name on green"></section>
</body>
</html>
```